Billboard Design for Harbor Lane Dentistry

Brookhaven Family Dental Care
Phone number: 318-562-0913
Address: 248 Castleford Blvd
Hours: 7am-5pm ; Monday-Friday

Dental Implant Surgery
Same Day Emergency Visits
Cosmetic Treatments
GLINT! Whitening

NAMES: Dr. Colin Varnstaad
Dr. Peter Ashdale

MOST INSURANCES ACCEPTED

Eye catching slogan/colors/design for billboard

Our website is www.brookhavenfamilydentalcare.example to see current branding.

Target Market(s)

Target market is anyone in Alexandria. Focus on Families and High End Cosmetic Dentistry.

Industry/Entity Type

Dental Clinic

Requirements
Must have
• Brookhaven Family Dental Care
• Phone number: 318-562-0913
• Address: 248 Castleford Blvd
• Hours: 7am-5pm ; Monday-Friday
• Dental Implant Surgery
• Same Day Emergency Visits
• Cosmetic Treatments
• GLINT! Whitening
• NAMES: Dr. Colin Varnstaad
• Dr. Peter Ashdale
• and logo
Nice to have
• digital billboard-try to catch attention with color or phrase
Should not have
• Can not make claims or compare to other area dentist's according to laws.

```html
<!DOCTYPE html>
<html lang="en">
<head>
<meta charset="utf-8">
<title>Brookhaven Family Dental Care — Billboard</title>
<link rel="stylesheet" href="https://fonts.googleapis.com/css2?family=Open+Sans:wght@400;600&family=Roboto+Condensed:wght@400;700&family=Roboto:wght@400&display=swap">
<style>
  :root {
    --sky: #5bc6de;
    --sky-deep: #3fa9c4;
    --mist: #e7f6fa;
    --panel: rgba(255, 255, 255, 0.55);
    --teal-text: #4fbfd9;
    --grey-text: #9a9a9a;
    --grey-dark: #8c8c8c;
    --check: #7f959b;
    --white: #ffffff;
  }
  * { margin: 0; padding: 0; box-sizing: border-box; }
  html, body { width: 1200px; height: 571px; overflow: hidden; background: var(--white); }
  .billboard {
    position: relative;
    width: 1200px;
    height: 571px;
    overflow: hidden;
    background: var(--mist);
    font-family: "Open Sans", Arial, sans-serif;
  }
  .sky-band {
    position: absolute; left: 0; top: 0;
    width: 1200px; height: 286px;
    background: var(--sky);
  }
  .portrait {
    position: absolute; left: 0; top: 0;
    width: 745px; height: 571px;
    background: linear-gradient(180deg, #3e9fb6 0%, #5db4c8 45%, #b9dde6 78%, rgba(231,246,250,0) 100%);
  }
  .info-panel {
    position: absolute; left: 0; top: 286px;
    width: 705px; height: 285px;
    background: linear-gradient(90deg, rgba(255,255,255,0.45), var(--panel) 70%, rgba(255,255,255,0));
  }
  .services {
    position: absolute; left: 802px; top: 60px;
    list-style: none;
  }
  .services li {
    display: flex; align-items: center;
    height: 41px;
    color: var(--white);
    font-size: 17.5px;
    letter-spacing: 0.3px;
    text-transform: uppercase;
  }
  .services svg { width: 33px; height: 33px; margin-right: 14px; flex: none; }
  .slogan {
    position: absolute; left: 0; top: 300px;
    width: 806px; text-align: center;
    color: var(--teal-text);
    font-weight: 400;
    line-height: 1;
  }
  .slogan .lead { display: block; font-size: 38px; letter-spacing: 0.5px; }
  .slogan .punch { display: block; font-size: 49px; font-weight: 600; margin-top: 8px; }
  .call-line {
    position: absolute; left: 0; top: 431px;
    width: 806px; text-align: center;
    font-family: "Roboto Condensed", Arial Narrow, sans-serif;
    font-size: 29px;
    color: var(--grey-text);
    letter-spacing: 0.3px;
  }
  .call-line strong { color: var(--grey-dark); font-weight: 700; }
  .contact {
    position: absolute; top: 480px;
    display: flex; align-items: center;
    font-family: "Roboto", Arial, sans-serif;
    font-size: 16.5px; line-height: 22px;
    color: var(--grey-text);
  }
  .contact svg { flex: none; margin-right: 12px; }
  .contact--doctors { left: 134px; }
  .contact--location { left: 411px; }
  .brand-name {
    position: absolute; left: 790px; top: 395px;
    width: 340px; text-align: center;
    color: var(--teal-text);
    font-weight: 600;
    text-transform: uppercase;
    line-height: 1;
  }
  .brand-name .main { display: block; font-size: 38px; letter-spacing: 1px; }
  .brand-name .sub { display: block; font-size: 16px; letter-spacing: 4.5px; margin-top: 8px; }
</style>
</head>
<body>
<main class="billboard">
  <div class="sky-band"></div>
  <div class="portrait" role="img" aria-label="Close-up portrait of a smiling man, tinted in blue"></div>
  <div class="info-panel"></div>

  <ul class="services">
    <li><svg viewBox="0 0 33 33" aria-hidden="true"><rect x="2" y="6" width="24" height="24" fill="none" stroke="var(--check)" stroke-width="2.5"/><path d="M8 17l6 6L31 4" fill="none" stroke="var(--check)" stroke-width="4"/></svg>Dental Implant Surgery</li>
    <li><svg viewBox="0 0 33 33" aria-hidden="true"><rect x="2" y="6" width="24" height="24" fill="none" stroke="var(--check)" stroke-width="2.5"/><path d="M8 17l6 6L31 4" fill="none" stroke="var(--check)" stroke-width="4"/></svg>Same Day Emergency Visits</li>
    <li><svg viewBox="0 0 33 33" aria-hidden="true"><rect x="2" y="6" width="24" height="24" fill="none" stroke="var(--check)" stroke-width="2.5"/><path d="M8 17l6 6L31 4" fill="none" stroke="var(--check)" stroke-width="4"/></svg>Cosmetic Treatments</li>
    <li><svg viewBox="0 0 33 33" aria-hidden="true"><rect x="2" y="6" width="24" height="24" fill="none" stroke="var(--check)" stroke-width="2.5"/><path d="M8 17l6 6L31 4" fill="none" stroke="var(--check)" stroke-width="4"/></svg>GLINT! Whitening</li>
  </ul>

  <h1 class="slogan"><span class="lead">WE’LL MAKE YOU</span><span class="punch">SMILE!</span></h1>

  <p class="call-line">CALL US ON <strong>318-562-0913</strong> TODAY!</p>

  <div class="contact contact--doctors">
    <svg width="46" height="46" viewBox="0 0 46 46" aria-hidden="true">
      <circle cx="23" cy="14" r="9" fill="none" stroke="var(--grey-text)" stroke-width="2"/>
      <path d="M6 44c0-11 7-17 17-17s17 6 17 17" fill="none" stroke="var(--grey-text)" stroke-width="2"/>
      <path d="M15 29v7a4 4 0 0 0 8 0" fill="none" stroke="var(--grey-text)" stroke-width="2"/>
      <circle cx="31" cy="37" r="3" fill="none" stroke="var(--grey-text)" stroke-width="2"/>
      <path d="M31 29v5" stroke="var(--grey-text)" stroke-width="2"/>
    </svg>
    <span>Dr. Colin Varnstaad<br>Dr. Peter Ashdale</span>
  </div>

  <div class="contact contact--location">
    <svg width="34" height="46" viewBox="0 0 34 46" aria-hidden="true">
      <path d="M17 44C8 31 3 24 3 16a14 14 0 0 1 28 0c0 8-5 15-14 28z" fill="none" stroke="var(--grey-text)" stroke-width="2.2"/>
      <circle cx="17" cy="16" r="5.5" fill="none" stroke="var(--grey-text)" stroke-width="2.2"/>
    </svg>
    <span>248 Castleford Blvd<br>7am-5pm, Monday-Friday</span>
  </div>

  <p class="brand-name"><span class="main">Brookhaven</span><span class="sub">Family Dental Care</span></p>
</main>
</body>
</html>
```